Retail korea clothing store needs a logo desgin

Retail clothing store. Our main customer is 28-35 years women. our store is located at japan town San Francisco. our theme color are black , White and sliver color. we would like modern.

Clothing

```html
<!DOCTYPE html>
<html lang="en">
<head>
<meta charset="utf-8">
<title>Velora – Business Card Front and Back</title>
<link rel="stylesheet" href="https://fonts.googleapis.com/css2?family=Quicksand:wght@500;700&display=swap">
<style>
  :root {
    --stage: #ebebeb;
    --card: #ffffff;
    --edge: #5e5e5e;
    --ink: #555555;
    --ink-soft: #6a6a6a;
    --block: #e4e4e4;
    --rule: #4a4a4a;
  }
  * { margin: 0; padding: 0; box-sizing: border-box; }
  html, body {
    width: 1200px; height: 665px; overflow: hidden;
    background: var(--stage);
    font-family: "Quicksand", sans-serif;
    color: var(--ink);
  }
  .stage {
    position: relative; width: 1200px; height: 665px;
    display: flex; justify-content: center; align-items: center; gap: 60px;
  }
  .card {
    position: relative; width: 480px; height: 272px;
    background: var(--card);
    border-top: 10px solid var(--edge);
    border-bottom: 10px solid var(--edge);
    overflow: hidden;
  }
  .card__block {
    position: absolute; background: var(--block);
  }
  /* front */
  .card--front .card__block { left: 180px; top: 80px; width: 250px; height: 150px; }
  .brand { position: absolute; left: 28px; top: 26px; }
  .brand__name {
    font-weight: 700; font-size: 40px; line-height: 1; color: var(--ink);
    letter-spacing: 0.5px;
  }
  .brand__rule { width: 150px; height: 2px; background: var(--rule); margin: 6px 0 4px; }
  .brand__tag { font-weight: 700; font-size: 10px; letter-spacing: 0.6px; color: var(--ink); }
  .contact { position: absolute; left: 150px; top: 120px; }
  .contact__name { font-weight: 700; font-size: 30px; color: var(--ink); }
  .contact__lines {
    list-style: none; margin: 4px 0 0 70px;
    font-weight: 500; font-size: 13px; line-height: 1.55; color: var(--ink-soft);
  }
  /* back */
  .card--back .card__block { left: 110px; top: 45px; width: 260px; height: 162px; }
  .card--back .brand { left: 0; right: 0; top: 80px; text-align: center; }
  .card--back .brand__name { font-size: 60px; }
  .card--back .brand__tag { font-weight: 500; font-size: 14px; letter-spacing: 1px; margin-top: 6px; }
</style>
</head>
<body>
<main class="stage">
  <section class="card card--front" aria-label="Business card front">
    <div class="card__block"></div>
    <div class="brand">
      <div class="brand__name">Velora</div>
      <div class="brand__rule"></div>
      <div class="brand__tag">RETAIL CLOTHING STORE</div>
    </div>
    <div class="contact">
      <div class="contact__name">Your name here</div>
      <ul class="contact__lines">
        <li>Your phone</li>
        <li>Your email</li>
        <li>Your websites</li>
      </ul>
    </div>
  </section>
  <section class="card card--back" aria-label="Business card back">
    <div class="card__block"></div>
    <div class="brand">
      <div class="brand__name">Velora</div>
      <div class="brand__tag">RETAIL CLOTHING STORE</div>
    </div>
  </section>
</main>
</body>
</html>
```